Specialist Technical Theatre service for schools

The task is to design a brochure (A5, 4 pages) for mailing to secondary/high school heads and drama departments to sell them our services as Technical Theatre and Drama professionals who can help them to offer elements of a curriculum that they do not currently offer as well as raise the technical standards of their school productions.
Please find a document attached which outlines the content for the brochure. Please read the document first so that you understand our aims. The text highlighted in yellow takes priority - the text highlighted in blue could be used if there is space.
Photos which may be used available on https://www.snapvault.example/photos/ben_torvik/ (please do not use watermarked morrow pictures).
Logo is attached (two variants) - one of which should appear somewhere on the design. Website address is www.bentorvik.co.uk and email is info@bentorvik.co.uk
Target Market(s)
Theatre and Drama teachers in Secondary/High schools
Headteachers of Secondary/High Schools
Industry/Entity Type
Education
Look and feel

```html
<!DOCTYPE html>
<html lang="en">
<head>
<meta charset="utf-8">
<title>Ben Torvik – Stage and Production Management brochure</title>
<link rel="stylesheet" href="https://fonts.googleapis.com/css2?family=EB+Garamond:wght@400;500&family=Open+Sans:ital,wght@0,400;0,600;0,700;1,400;1,700&display=swap">
<style>
  :root {
    --backdrop: #5b6a5c;
    --charcoal: #1f1d1f;
    --charcoal-soft: #2a2729;
    --navy: #2c3556;
    --navy-deep: #1c2240;
    --logo-blue: #3b4779;
    --gold: #b79a5c;
    --gold-light: #e2cd94;
    --paper: #f1f1f3;
    --text-light: #e9e9ee;
    --badge-purple: #5a2a7c;
    --badge-blue: #24306f;
    --badge-yellow: #e6cf3a;
    --badge-grey: #dcdce0;
  }
  * { box-sizing: border-box; margin: 0; padding: 0; }
  html, body { width: 1200px; height: 789px; overflow: hidden; }
  body { background: var(--backdrop); font-family: "Open Sans", Arial, sans-serif; position: relative; }

  .spread { position: absolute; left: 42px; top: 0; width: 1116px; height: 789px; display: flex; }
  .page { position: relative; width: 558px; height: 789px; overflow: hidden; }

  /* Back cover */
  .back-cover { background: var(--charcoal); }
  .contact-bar {
    position: absolute; top: 70px; left: 0; right: 0; height: 40px;
    background: var(--navy); color: var(--text-light);
    font-size: 15px; font-weight: 700; letter-spacing: .3px;
    display: flex; align-items: center; justify-content: center;
  }
  .contact-bar .divider { margin: 0 8px; font-weight: 400; }
  .intro { position: absolute; top: 132px; left: 44px; right: 44px; color: var(--text-light); text-align: center; }
  .intro-title { font-size: 16px; font-weight: 700; line-height: 1.3; margin-bottom: 12px; }
  .intro-body { font-size: 11px; line-height: 1.45; margin-bottom: 14px; }
  .intro-question { font-size: 11px; font-weight: 700; font-style: italic; line-height: 1.45; margin-bottom: 4px; }
  .intro-source { font-size: 10.5px; font-style: italic; }

  .lower-panel { position: absolute; top: 500px; left: 0; right: 0; bottom: 0; background: var(--paper); }

  .pattern-band { position: absolute; left: 0; right: 0; height: 74px; }
  .back-cover .pattern-band { top: 448px; }
  .front-cover .pattern-band { top: 352px; }

  .logo-disc {
    position: absolute; width: 230px; height: 230px; border-radius: 50%;
    background: radial-gradient(circle at 50% 40%, #6c78a8 0%, var(--logo-blue) 45%, var(--navy-deep) 100%);
    display: flex; align-items: center; justify-content: center; text-align: center;
    font-family: "EB Garamond", Georgia, serif; font-size: 44px; line-height: 1.05; color: #ffffff;
  }
  .back-cover .logo-disc { left: 128px; top: 372px; }
  .front-cover .logo-disc { left: 70px; top: 272px; }

  .partner-row { position: absolute; left: 0; right: 0; bottom: 58px; display: flex; justify-content: center; align-items: center; gap: 26px; }
  .partner-badge { display: block; }

  /* Front cover */
  .front-cover { background: var(--charcoal); }
  .cover-photo {
    position: absolute; top: 0; left: 0; right: 0; height: 380px;
    background:
      radial-gradient(ellipse 90px 150px at 42% 42%, rgba(225,225,235,.55), transparent 70%),
      linear-gradient(100deg, #2a2438 0%, #4a4266 35%, #2f3fb8 62%, #3a55e0 80%, #1a2466 100%);
  }
  .cover-title {
    position: absolute; left: 0; right: 0; top: 556px; text-align: center;
    font-family: "EB Garamond", Georgia, serif; font-size: 27px; letter-spacing: 1.5px;
    color: #ffffff; line-height: 1.3; text-transform: uppercase;
  }
</style>
</head>
<body>
<main class="spread">

  <section class="page back-cover">
    <div class="contact-bar">
      <span>www.bentorvik.co.uk</span><span class="divider">|</span><span>info@bentorvik.co.uk</span>
    </div>

    <div class="intro">
      <h2 class="intro-title">School Technical Theatre support<br>by Industry professionals.</h2>
      <p class="intro-body">As live theatre and performance becomes an increasingly important part of the global economy, there is currently a huge demand for Technical and Production Management professionals. We are able to support you with training your students in the specialist skills and knowledge of managing creative processes from initial concept through rehearsal to realised performance.</p>
      <p class="intro-question">With 60% of marks being allocated to the practical elements of ‘creating original drama’ and ‘making theatre’ you would like to offer your students the opportunity to pursue the technical design elements of the course but don’t have the technical support?</p>
      <p class="intro-source">NQB A-level Drama and Theatre and Examwell GCSE Drama (from September 2016)</p>
    </div>

    <div class="lower-panel"></div>

    <svg class="pattern-band" viewBox="0 0 558 74" preserveAspectRatio="none" role="img" aria-label="Monogram pattern band">
      <rect width="558" height="74" fill="#171517"/>
      <rect y="0" width="558" height="3" fill="var(--gold)"/>
      <rect y="8" width="558" height="1.5" fill="var(--gold-light)"/>
      <rect y="64.5" width="558" height="1.5" fill="var(--gold-light)"/>
      <rect y="71" width="558" height="3" fill="var(--gold)"/>
    </svg>

    <div class="logo-disc">Ben<br>Torvik</div>

    <div class="partner-row">
      <svg class="partner-badge" width="70" height="34" aria-label="Partner badge" role="img"><rect width="70" height="34" rx="4" fill="var(--badge-purple)"/></svg>
      <svg class="partner-badge" width="44" height="44" aria-label="Partner badge" role="img"><rect width="44" height="44" fill="var(--badge-blue)"/></svg>
      <svg class="partner-badge" width="46" height="46" aria-label="Partner badge" role="img"><circle cx="23" cy="23" r="23" fill="var(--badge-yellow)"/></svg>
      <svg class="partner-badge" width="62" height="52" aria-label="Certificate badge" role="img"><rect width="62" height="52" rx="3" fill="var(--badge-grey)"/></svg>
    </div>
  </section>

  <section class="page front-cover">
    <div class="cover-photo" role="img" aria-label="Night photograph of a performer in a large winged costume in front of a blue-lit glass building"></div>

    <svg class="pattern-band" viewBox="0 0 558 74" preserveAspectRatio="none" role="img" aria-label="Monogram pattern band">
      <rect width="558" height="74" fill="#171517"/>
      <rect y="0" width="558" height="3" fill="var(--gold)"/>
      <rect y="8" width="558" height="1.5" fill="var(--gold-light)"/>
      <rect y="64.5" width="558" height="1.5" fill="var(--gold-light)"/>
      <rect y="71" width="558" height="3" fill="var(--gold)"/>
    </svg>

    <div class="logo-disc">Ben<br>Torvik</div>

    <h1 class="cover-title">Stage and<br>Production Management</h1>
  </section>

</main>
</body>
</html>
```